Velmo BUSINESS CARD

Design an attention-grabbing business cards. Draw inspiration from the provided logo file. Please use the same font style as in the logo.
the back side of the card is for accent/decoration.

Contact Information for Business Card

PLEASE USE PROVIDED BUSINESS CARD SAMPLE

Other font styles liked:
• LUMETTE

Colors
EB3D1F
EC4F4E
F09395
F8D3D4
FCEDEE

Requirements
Must have
• RED, BLACK COLORS, SOLID BACK COLOR
Nice to have
• MAKE IT FANCY

```html
<!DOCTYPE html>
<html lang="en">
<head>
<meta charset="UTF-8">
<title>Velmo Business Card</title>
<link href="https://fonts.googleapis.com/css2?family=Poppins:wght@300;400;600;700&display=swap" rel="stylesheet">
<style>
  :root {
    --stage: #2b2b2b;
    --card-dark: #1b1b1c;
    --card-light: #ffffff;
    --ink: #161616;
    --mark-light: #e1e3e2;
    --red: #e8202a;
    --rule: #9a9a9a;
  }
  * { margin: 0; padding: 0; box-sizing: border-box; }
  html, body { width: 1200px; height: 1040px; overflow: hidden; }
  body {
    background: var(--stage);
    font-family: "Poppins", sans-serif;
    position: relative;
  }
  .card {
    position: absolute;
    left: 250px;
    width: 700px;
    height: 400px;
    border-radius: 0 90px 0 90px;
  }
  .card-back { top: 60px; background: var(--card-dark); }
  .card-front { top: 540px; background: var(--card-light); color: var(--ink); }

  .brand { position: absolute; display: flex; flex-direction: column; align-items: flex-start; }
  .brand-row { display: flex; align-items: center; gap: 14px; }
  .brand-square { display: block; }
  .brand-name { font-weight: 600; letter-spacing: 4px; line-height: 1; }
  .brand-tagline { font-weight: 300; text-transform: uppercase; letter-spacing: 3px; }

  .card-back .brand { left: 120px; top: 140px; }
  .card-back .brand-square { width: 90px; height: 90px; background: var(--mark-light); }
  .card-back .brand-name { font-size: 78px; color: var(--mark-light); }
  .card-back .brand-tagline { font-size: 13px; color: var(--mark-light); margin: 10px 0 0 180px; }

  .card-front .brand { left: 60px; top: 150px; }
  .card-front .brand-square { width: 56px; height: 56px; background: var(--ink); }
  .card-front .brand-name { font-size: 50px; color: var(--ink); }
  .card-front .brand-tagline { font-size: 9px; color: var(--ink); margin: 6px 0 0 90px; }

  .divider {
    position: absolute; left: 355px; top: 80px;
    width: 1px; height: 240px; background: var(--rule);
  }
  .contact { position: absolute; left: 385px; top: 82px; }
  .person-name { font-size: 26px; font-weight: 700; letter-spacing: 2px; text-transform: uppercase; line-height: 1.1; }
  .person-title { font-size: 19px; color: var(--red); line-height: 1.2; margin-bottom: 18px; }
  .contact-list { list-style: none; }
  .contact-list li { display: flex; align-items: center; gap: 10px; font-size: 18px; line-height: 1.45; }
  .contact-list svg { width: 17px; height: 17px; flex: none; }
  .accent { color: var(--red); }
  .address { font-size: 18px; line-height: 1.3; margin-top: 18px; }
</style>
</head>
<body>
  <section class="card card-back">
    <div class="brand">
      <div class="brand-row">
        <span class="brand-square"></span>
        <span class="brand-name">VELMO</span>
      </div>
      <span class="brand-tagline">Freight Moved Right</span>
    </div>
  </section>

  <section class="card card-front">
    <div class="brand">
      <div class="brand-row">
        <span class="brand-square"></span>
        <span class="brand-name">VELMO</span>
      </div>
      <span class="brand-tagline">Freight Moved Right</span>
    </div>

    <div class="divider"></div>

    <div class="contact">
      <p class="person-name">Adrian Holt</p>
      <p class="person-title">President</p>
      <ul class="contact-list">
        <li>
          <svg viewBox="0 0 24 24" fill="none" stroke="#e8202a" stroke-width="2.2" stroke-linecap="round" stroke-linejoin="round" aria-hidden="true"><path d="M5 3h4l2 5-2.5 1.5a11 11 0 0 0 6 6L16 13l5 2v4a2 2 0 0 1-2 2A17 17 0 0 1 3 5a2 2 0 0 1 2-2z"/></svg>
          555-014-2736
        </li>
        <li>
          <svg viewBox="0 0 24 24" fill="none" stroke="#e8202a" stroke-width="2.2" stroke-linecap="round" aria-hidden="true"><rect x="6" y="2" width="12" height="20" rx="2"/><line x1="11" y1="18" x2="13" y2="18"/></svg>
          555-019-4821
        </li>
        <li>
          <svg viewBox="0 0 24 24" fill="none" stroke="#e8202a" stroke-width="2.2" stroke-linejoin="round" aria-hidden="true"><rect x="2" y="5" width="20" height="14"/><path d="M2 5l10 8 10-8"/></svg>
          AHolt@velmo-llc.com
        </li>
        <li>
          <svg viewBox="0 0 24 24" fill="none" stroke="#e8202a" stroke-width="2" aria-hidden="true"><circle cx="12" cy="12" r="10"/><ellipse cx="12" cy="12" rx="4.5" ry="10"/><line x1="2" y1="12" x2="22" y2="12"/><line x1="4" y1="7" x2="20" y2="7"/><line x1="4" y1="17" x2="20" y2="17"/></svg>
          <span>www.<span class="accent">Velmo-LLC</span>.com</span>
        </li>
      </ul>
      <p class="address">1480 N. Harlow Road<br>Brookfield, IN 46000</p>
    </div>
  </section>
</body>
</html>
```